Velmor PashuのRTZの電子書籍表紙デザインをお願いします。

*週末ごとに和みを探す読者へ贈る癒やしの四季手帳*というタイトルの表紙デザインの発注です。
サブタイトル 猫の昼寝は街を照らす
猫の昼寝は毎日を照らす
私は猫の昼寝に癒された
になります。
お笑い要素の多い1日1笑いみたいな本の表紙です。

初めての表紙デザイン依頼なので、よく勝手がわかっていませんので、
出来上がったデザインを作家グループの中で投票にかけて、
一番投票得票数の多かったものを表紙デザインとして選ばせていただきたいと考えております。
もしかしたら、その中で、何か修正依頼など来るかもしれませんが、
それも含めて、ご対応していただける方よろしくお願いします。

1部内容の抜粋を記載します。

その他何かご不明な点がございましたら、お気軽にご質問下さい。
よろしくお願いいたします。
すいません。作家名は後でお伝えします。作家名もどこかに挿入いただきたいです。よろしくお願いします。
データサイズですが、推奨サイズでJPEGファイルでご納品下さい、よろしくお願いします。
皆様、たくさんのご応募まことにありがとうございました。
現在、作家グループへ全体回覧のメールを致しました。
皆様の投票結果までお待ちください。
また、この度、いろいろな作品に触れさせていただきましたこと本当に
本当に感謝いたします。
今回の表紙に関しましては、どうしても1名しか選べない状況がございますこと
また、選挙による投票にて決定致しますこと、ご理解何卒よろしくお願い申しあげます。
また、もしも、今回当選に至らないことがありましても、
今後も私自身は作家生活を継続予定ですので、
(今回は作品の表紙に合わないことがあっても)作風の気に入ったデザイナー様には
個人的にお話を相談させていただく場合もあると思っております。
その際には何卒よろしくお願い申し上げます。この度はまことにありがとうございました。
この度はご応募まことにありがとうございました。厳選なる選挙の結果、1名の作家さんが選ばれました。
選ばれました方には個別にお伝えいたしております。この度はまことにご応募ありがとうございました。

作家メンバーによる総選挙にて決定させて頂きました。皆様に広く愛される作品で、投票数も多く選ばせて頂きました。誠にありがとうございました。

今回、誠にご提案ありがとうございました。私自身は作家活動を継続していくつもりですので、また、個別にご依頼させて頂くこともあるかと思います。その時はよろしくお願いします。この度はありがとうございました。

```html
<!DOCTYPE html>
<html lang="ja">
<head>
<meta charset="utf-8">
<title>週末ごとに和みを探す読者へ贈る癒やしの四季手帳</title>
<link rel="stylesheet" href="https://fonts.googleapis.com/css2?family=Noto+Sans+JP:wght@500;700;900&display=swap">
<style>
  :root {
    --paper: #ffffff;
    --ink: #111111;
    --accent: #f39a1e;
    --header-yellow: #fcc21b;
    --card-edge: #d9d9d9;
    --card-shade: #eeeeee;
    --rule: #555555;
  }
  * { margin: 0; padding: 0; box-sizing: border-box; }
  html, body { width: 750px; height: 1200px; overflow: hidden; background: var(--paper); }
  body { font-family: "Noto Sans JP", sans-serif; color: var(--ink); }
  .cover { position: relative; width: 750px; height: 1200px; background: var(--paper); }

  .tagline-left, .tagline-right {
    position: absolute; writing-mode: vertical-rl; font-weight: 900; line-height: 1;
  }
  .tagline-left { left: 58px; top: 40px; font-size: 52px; letter-spacing: 1px; }
  .tagline-right { right: 58px; top: 40px; font-size: 44px; letter-spacing: 2px; }

  .title {
    position: absolute; left: 0; right: 0; top: 140px; text-align: center;
    font-weight: 900; font-size: 78px; line-height: 1.45;
  }
  .title .accent { color: var(--accent); }

  .calendar {
    position: absolute; left: 212px; top: 385px; width: 400px; height: 545px;
  }
  .calendar-body {
    position: absolute; inset: 0; background: var(--paper);
    border: 3px solid var(--card-edge); border-radius: 26px;
    box-shadow: 0 6px 14px rgba(0,0,0,0.12);
    overflow: hidden;
  }
  .calendar-header {
    height: 150px; background: var(--header-yellow);
    display: flex; align-items: center; justify-content: center;
    font-weight: 900; font-size: 80px; letter-spacing: 6px;
    border-bottom: 4px solid #e7ab10;
  }
  .calendar-rings { position: absolute; left: 0; top: -18px; width: 400px; height: 50px; }
  .calendar-art {
    position: absolute; left: 122px; top: 205px; width: 156px; height: 150px;
    border-radius: 48% 52% 46% 54%;
    background: radial-gradient(circle at 50% 45%, #ffffff 0%, #f2f2f2 70%, #e2e2e2 100%);
    border: 4px solid #222;
  }
  .author {
    position: absolute; left: 0; right: 0; top: 455px; text-align: center;
    font-size: 25px; font-weight: 700;
  }
  .calendar-curl { position: absolute; right: -3px; bottom: -3px; width: 90px; height: 90px; }

  .subtitles {
    position: absolute; left: 0; right: 0; top: 1000px; height: 155px;
    border-top: 2px solid var(--rule); border-bottom: 2px solid var(--rule);
    display: flex;
  }
  .subtitle {
    flex: 1; display: flex; flex-direction: column; align-items: center; justify-content: center;
    text-align: center; line-height: 1.35;
  }
  .subtitle + .subtitle { border-left: 2px solid var(--rule); }
  .subtitle .small { font-size: 18px; font-weight: 500; }
  .subtitle .big { font-size: 29px; font-weight: 700; margin-top: 8px; }
  .subtitle .big-top { font-size: 29px; font-weight: 700; margin-bottom: 4px; }
  .subtitle .small + .big.tight { margin-top: 4px; }
</style>
</head>
<body>
  <main class="cover">
    <div class="tagline-left">和みを探す読者へ贈る</div>
    <div class="tagline-right">週末ごとに</div>

    <h1 class="title"><span class="accent">癒</span>やしの<br>四季</h1>

    <section class="calendar">
      <div class="calendar-body">
        <div class="calendar-header">手帳</div>
        <div class="calendar-art" role="img" aria-label="笑顔のキャラクターのイラスト"></div>
        <p class="author">森川陽介［著］</p>
      </div>
      <svg class="calendar-rings" viewBox="0 0 400 50" aria-hidden="true">
        <rect x="80" y="4" width="16" height="42" rx="8" fill="#ffffff" stroke="#bbbbbb" stroke-width="3"/>
        <rect x="304" y="4" width="16" height="42" rx="8" fill="#ffffff" stroke="#bbbbbb" stroke-width="3"/>
      </svg>
      <svg class="calendar-curl" viewBox="0 0 90 90" aria-hidden="true">
        <path d="M90 0 L90 90 L0 90 Q55 70 90 0 Z" fill="var(--paper)"/>
        <path d="M0 90 Q55 70 90 0 Q40 30 20 70 Z" fill="var(--card-shade)" stroke="var(--card-edge)" stroke-width="3"/>
      </svg>
    </section>

    <section class="subtitles">
      <div class="subtitle">
        <span class="small">猫の昼寝は</span>
        <span class="big">街を照らす</span>
      </div>
      <div class="subtitle">
        <span class="small">猫の昼寝は</span>
        <span class="big">毎日を照らす</span>
      </div>
      <div class="subtitle">
        <span class="big-top">私は</span>
        <span class="small">猫の昼寝に</span>
        <span class="big tight">癒された</span>
      </div>
    </section>
  </main>
</body>
</html>
```